Boutique Financial Services/Advisor Business Needs Web Design

Looking for an informational and functional web design for my Financial Services/Financial Advisement business. It should have functionality for Company name, address, phone #, "About Us", Who we are, Our Mission, Services we offer, Biographies/Photos of/about "The Team", and possibly a link to "Contact Us". Would like to see something new & exciting blended with a traditional/professional look that will appeal to those approaching retirement, as well as those younger clients that are beginning to think about planning for the future. I already have a web domain through Brixwell, but would like this to be the design we use for that domain.
Financial Services/Financial Advisor
Coded - Design and coding required
1 page

```html
<!DOCTYPE html>
<html lang="en">
<head>
<meta charset="utf-8">
<title>Summitline Wealth Management</title>
<link href="https://fonts.googleapis.com/css2?family=EB+Garamond:wght@500;600;700&family=Poppins:wght@400;500;600&display=swap" rel="stylesheet">
<style>
:root{
  --navy:#0f0f4a;
  --navy-deep:#0a0a38;
  --ink:#1b1b2e;
  --text:#55556a;
  --muted:#8a8a99;
  --line:#dcdce4;
  --paper:#ffffff;
  --mist:#f2f2f5;
  --gold:#e8c77a;
}
*{box-sizing:border-box;margin:0;padding:0}
html,body{width:1200px;height:3152px;overflow:hidden}
body{position:relative;background:var(--paper);font-family:"Poppins",Arial,sans-serif;color:var(--text)}
.serif{font-family:"EB Garamond",Georgia,serif}
section,header,footer{position:absolute;left:0;width:1200px}
a{color:inherit;text-decoration:none}

/* header */
.site-header{top:0;height:112px;background:var(--paper);box-shadow:0 2px 8px rgba(0,0,0,.06)}
.topbar{position:absolute;right:0;top:0;width:600px;height:28px;background:var(--navy);color:#fff;font-size:11px;display:flex;align-items:center;gap:40px;padding-left:70px}
.topbar span{display:flex;align-items:center;gap:8px}
.brand{position:absolute;left:100px;top:22px;width:230px;color:var(--navy);font-family:"EB Garamond",Georgia,serif;font-weight:700;text-align:center;line-height:1}
.brand .b1{font-size:24px;letter-spacing:1px}
.brand .b2{font-size:15px;letter-spacing:4px;margin-top:4px}
.nav{position:absolute;left:440px;top:58px;display:flex;gap:30px;font-size:15px;color:var(--ink);font-weight:500}
.nav .active{color:var(--navy);font-weight:600}
.btn{display:inline-block;background:var(--navy);color:#fff;font-size:15px;font-weight:500;padding:12px 26px;border-radius:2px}
.header-cta{position:absolute;left:935px;top:48px}

/* hero */
.hero{top:112px;height:468px;background:linear-gradient(100deg,#c9cbd3 0%,#9ea4b4 35%,#3a3d66 55%,#14144d 72%,#101046 100%)}
.hero-photo{position:absolute;left:0;top:0;width:640px;height:468px;background:radial-gradient(ellipse at 45% 55%,rgba(255,255,255,.55),rgba(255,255,255,0) 60%)}
.hero-copy{position:absolute;left:620px;top:80px;width:440px;text-align:center;color:#fff}
.hero-copy .kicker{font-size:24px;letter-spacing:1px;font-weight:600}
.hero-copy h1{font-size:52px;line-height:1.05;font-weight:600;margin-top:6px;letter-spacing:1px}
.hero-copy .rule{width:400px;height:1px;background:rgba(255,255,255,.6);margin:22px auto 18px}
.hero-copy .tag{font-size:19px;letter-spacing:1px;font-weight:500}
.hero-copy .tag b{color:var(--gold);font-weight:600}
.hero-copy .btn{margin-top:30px;background:#9b9bb3;color:#fff;font-size:14px;padding:12px 28px}

/* about / mission */
.about{top:580px;height:440px}
.about-left{position:absolute;left:100px;top:50px;width:420px}
.about-left h2{font-size:52px;color:var(--ink);font-weight:600;letter-spacing:1px}
.about-left .rule{width:380px;height:2px;background:var(--ink);margin:4px 0 22px}
.about-left p{font-size:16px;line-height:1.55;margin-bottom:18px}
.about-left .btn{margin-top:14px;font-size:14px;padding:12px 22px}
.mission{position:absolute;left:590px;top:10px;width:610px;height:430px;background:var(--navy);color:#e4e4f0;text-align:center;padding:70px 70px 0}
.mission h2{font-size:42px;color:#fff;font-weight:600;margin-bottom:22px}
.mission p{font-size:16px;line-height:1.55;margin-bottom:22px}

/* services */
.services{top:1020px;height:720px;background:var(--mist)}
.sec-title{text-align:center;font-size:50px;color:var(--ink);font-weight:600;letter-spacing:1px}
.sec-title+.rule{width:90px;height:2px;background:var(--ink);margin:4px auto 0}
.services .sec-title{margin-top:80px}
.cards{position:absolute;left:110px;top:180px;display:flex;gap:30px}
.card{width:310px;height:320px;background:#fff;box-shadow:0 4px 14px rgba(0,0,0,.08);text-align:center;padding:44px 30px 0}
.card svg.icon{width:60px;height:60px}
.card h3{font-family:"Poppins",Arial,sans-serif;font-size:19px;font-weight:600;color:var(--ink);margin:22px 0 16px}
.card p{font-size:14px;line-height:1.6;color:var(--muted)}
.card .arrow{margin-top:24px}
.dots{position:absolute;left:550px;top:574px;display:flex;gap:8px}
.dots i{width:30px;height:4px;background:#cfcfd8;display:block}
.dots i:first-child{width:44px;background:var(--ink)}

/* team */
.team{top:1740px;height:560px}
.team .sec-title{margin-top:0;padding-top:0}
.team-grid{position:absolute;left:110px;top:104px;display:flex;gap:22px}
.member{position:relative;width:232px;height:308px;border-radius:6px;overflow:hidden}
.member .meta{position:absolute;left:16px;bottom:22px;color:#fff}
.member .meta b{display:block;font-size:15px;font-weight:600}
.member .meta span{font-size:12px}
.team .btn{position:absolute;left:530px;top:450px;font-size:14px;padding:12px 24px}

/* contact */
.contact{top:2300px;height:560px;background:linear-gradient(180deg,#f4f4f6,#ececf0)}
.contact .sec-title{padding-top:60px}
.form{position:absolute;left:280px;top:155px;width:640px}
.field{background:#fff;border:1px solid var(--line);font-size:13px;color:var(--muted);padding:16px 20px;height:56px}
.row{display:flex;gap:8px;margin-bottom:14px}
.row .field{flex:1}
.field.full{margin-bottom:14px}
.field.msg{height:106px}
.form .btn{display:block;width:140px;margin:16px auto 0;text-align:center;font-size:14px;padding:12px 0}

/* footer */
.site-footer{top:2860px;height:292px;background:var(--navy-deep);color:#dcdcec;font-size:14px}
.footer-brand{position:absolute;left:100px;top:60px;color:#fff;font-family:"EB Garamond",Georgia,serif;font-weight:700;text-align:center;width:270px;line-height:1}
.footer-brand .b1{font-size:30px}
.footer-brand .b2{font-size:19px;letter-spacing:5px;margin-top:6px}
.col{position:absolute;top:36px}
.col h4{font-family:"Poppins",Arial,sans-serif;font-size:15px;color:#fff;font-weight:600;margin-bottom:14px}
.col li{list-style:none;margin-bottom:8px;display:flex;gap:12px;align-items:flex-start;line-height:1.4}
.col-contact{left:470px}
.col-links{left:755px}
.col-other{left:945px}
.copy{position:absolute;left:0;right:0;top:250px;text-align:center;font-size:12px;color:#bcbcd0}
</style>
</head>
<body>

<header class="site-header">
  <div class="topbar">
    <span><svg width="10" height="13" viewBox="0 0 10 13"><path d="M5 0a5 5 0 0 1 5 5c0 3.5-5 8-5 8S0 8.5 0 5a5 5 0 0 1 5-5z" fill="#fff"/><circle cx="5" cy="5" r="2" fill="#0f0f4a"/></svg>Summitline Wealth Management, Harborview Plaza</span>
    <span><svg width="12" height="12" viewBox="0 0 12 12"><path d="M2 0l3 3-1.5 1.5a8 8 0 0 0 4 4L9 7l3 3-2 2C5 12 0 7 0 2z" fill="#fff"/></svg>+1 555-014-2290</span>
  </div>
  <div class="brand"><div class="b1">SUMMITLINE WEALTH</div><div class="b2">MANAGEMENT</div></div>
  <nav class="nav">
    <a class="active">Home</a><a>About Us</a><a>Services</a><a>Team</a><a>Blog</a><a>Contact Us</a>
  </nav>
  <a class="btn header-cta">Get A Quote</a>
</header>

<section class="hero">
  <div class="hero-photo" role="img" aria-label="Photo of a businessman's open hand holding a rising financial growth chart"></div>
  <div class="hero-copy serif">
    <div class="kicker">WELCOME TO</div>
    <h1>SUMMITLINE WEALTH MANAGEMENT</h1>
    <div class="rule"></div>
    <div class="tag" style="font-family:Poppins,Arial,sans-serif">GUIDING YOU TO YOUR <b>FINANCIAL SUMMIT</b></div>
    <a class="btn" style="font-family:Poppins,Arial,sans-serif">Get A Quote</a>
  </div>
</section>

<section class="about">
  <div class="about-left">
    <h2 class="serif">ABOUT US</h2>
    <div class="rule"></div>
    <p>Lorem ipsum dolor sit amet, consectetur adipiscing elit, sed do eiusmod tempor incididunt ut labore et dolore magna aliquaold sumnod tempor incididunt ut labore et dolore magna.</p>
    <p>Consectetur adipiscing elit, sed do sumnod tempor incididunt ut labore et dolore magna aliqui.</p>
    <a class="btn">Learn More</a>
  </div>
  <div class="mission">
    <h2 class="serif">Our Mission</h2>
    <p>Consectetur adipiscing elit, sed do sumnod tempor incididunt ut labore et dolore magna aliqui.</p>
    <p>Lorem ipsum dolor sit amet, consectetur adipiscing elited do eiusmod tempor incididunt ut labore et dolore magna aliqua. Ut enim ad minim veniam, quis nostrud exercitation ullamco laboris nisi ut aliquip ex ea commodo consequat. Duis aute irure dolor in reprehenderit in voluptate.</p>
  </div>
</section>

<section class="services">
  <h2 class="sec-title serif">OUR SERVICES</h2><div class="rule"></div>
  <div class="cards">
    <div class="card">
      <svg class="icon" viewBox="0 0 60 60" fill="none" stroke="#1b1b2e" stroke-width="2"><circle cx="30" cy="30" r="24"/><circle cx="30" cy="30" r="17"/><path d="M34 23c-1-2-3-3-5-3-3 0-5 2-5 4s2 3 6 4 6 2 6 5-2 4-6 4c-3 0-5-1-6-3M30 17v3M30 40v3"/></svg>
      <h3>Cash Management</h3>
      <p>Sed ut perspiciatis unde omnis iste natus error sit voluptatem accusan tium doloremque laudantium, totam remaque ab illo inventore.</p>
      <svg class="arrow" width="18" height="12" viewBox="0 0 18 12"><path d="M0 6h16M11 1l5 5-5 5" stroke="#1b1b2e" stroke-width="2" fill="none"/></svg>
    </div>
    <div class="card">
      <svg class="icon" viewBox="0 0 60 60" fill="none" stroke="#1b1b2e" stroke-width="2"><path d="M14 6h24l10 10v38H14z"/><path d="M38 6v10h10M20 26h20M20 33h20M20 40h12"/><circle cx="42" cy="46" r="8" fill="#fff"/><path d="M39 49l6-6M39 43h.1M45 49h.1"/></svg>
      <h3>Tax Planning</h3>
      <p>Sed ut perspiciatis unde omnis iste natus error sit voluptatem accusan tium doloremque laudantium, totam remaque ab illo inventore.</p>
      <svg class="arrow" width="18" height="12" viewBox="0 0 18 12"><path d="M0 6h16M11 1l5 5-5 5" stroke="#1b1b2e" stroke-width="2" fill="none"/></svg>
    </div>
    <div class="card">
      <svg class="icon" viewBox="0 0 60 60" fill="none" stroke="#1b1b2e" stroke-width="2"><rect x="16" y="20" width="30" height="34" rx="3"/><path d="M22 20v-8h18v8M28 10h6"/><path d="M34 28c-1-1-2-2-4-2s-4 1-4 3 2 2 4 3 4 1 4 3-2 3-4 3-3-1-4-2M30 24v2M30 40v2"/></svg>
      <h3>Retirement Planning</h3>
      <p>Sed ut perspiciatis unde omnis iste natus error sit voluptatem accusan tium doloremque laudantium, totam remaque ab illo inventore.</p>
      <svg class="arrow" width="18" height="12" viewBox="0 0 18 12"><path d="M0 6h16M11 1l5 5-5 5" stroke="#1b1b2e" stroke-width="2" fill="none"/></svg>
    </div>
  </div>
  <div class="dots"><i></i><i></i><i></i></div>
</section>

<section class="team">
  <h2 class="sec-title serif">OUR TEAM</h2><div class="rule"></div>
  <div class="team-grid">
    <div class="member" role="img" aria-label="Portrait photo of team member Jon Avery" style="background:linear-gradient(160deg,#8a8478,#3e3a36)">
      <div class="meta"><b>JON AVERY</b><span>Lorem ipsum set amet</span></div>
    </div>
    <div class="member" role="img" aria-label="Portrait photo of team member Harry Dale" style="background:linear-gradient(160deg,#c9c3bc,#6d625a)">
      <div class="meta"><b>HARRY DALE</b><span>Lorem ipsum set amet</span></div>
    </div>
    <div class="member" role="img" aria-label="Portrait photo of team member Mary Lowe" style="background:linear-gradient(160deg,#d8d6d2,#5d6a4a)">
      <div class="meta"><b>MARY LOWE</b><span>Lorem ipsum set amet</span></div>
    </div>
    <div class="member" role="img" aria-label="Portrait photo of team member Anna Pike" style="background:linear-gradient(160deg,#e2e2e4,#2d3550)">
      <div class="meta"><b>ANNA PIKE</b><span>Lorem ipsum set amet</span></div>
    </div>
  </div>
  <a class="btn">View More</a>
</section>

<section class="contact">
  <h2 class="sec-title serif">CONTACT US</h2><div class="rule"></div>
  <div class="form">
    <div class="row"><div class="field">Name *</div><div class="field">Phone *</div></div>
    <div class="field full">Email ID *</div>
    <div class="field msg">Message</div>
    <a class="btn">Submit Now</a>
  </div>
</section>

<footer class="site-footer">
  <div class="footer-brand"><div class="b1">SUMMITLINE WEALTH</div><div class="b2">MANAGEMENT</div></div>
  <div class="col col-contact">
    <h4>CONTACT</h4>
    <ul>
      <li><svg width="12" height="16" viewBox="0 0 10 13"><path d="M5 0a5 5 0 0 1 5 5c0 3.5-5 8-5 8S0 8.5 0 5a5 5 0 0 1 5-5z" fill="#fff"/><circle cx="5" cy="5" r="2" fill="#0a0a38"/></svg><span>Harborview Plaza,<br>Address Comes Here</span></li>
      <li><svg width="14" height="14" viewBox="0 0 12 12"><path d="M2 0l3 3-1.5 1.5a8 8 0 0 0 4 4L9 7l3 3-2 2C5 12 0 7 0 2z" fill="#fff"/></svg><span>+1 555-014-2290</span></li>
      <li><svg width="14" height="14" viewBox="0 0 14 14" fill="none" stroke="#fff" stroke-width="1.5"><circle cx="7" cy="7" r="6"/><path d="M1 7h12M7 1c-3 3-3 9 0 12M7 1c3 3 3 9 0 12"/></svg><span>hello@summitlinewm.com</span></li>
    </ul>
  </div>
  <div class="col col-links">
    <h4>QUICK LINKS</h4>
    <ul><li>Home</li><li>About Us</li><li>Solution</li><li>Blog</li></ul>
  </div>
  <div class="col col-other">
    <h4>OTHER LINKS</h4>
    <ul><li>Terms &amp; Conditions</li><li>Privacy Policy</li><li>FAQ</li><li>Contact</li></ul>
  </div>
  <div class="copy">2024 Summitline Wealth Management. All Rights Reserved.</div>
</footer>

</body>
</html>
```